Business card design needed

Financial planning company that specialises in super and insurance

I have attached my email with my logo so if you incorporate the logo please

Industry/Entity Type

Business

Contact Information for Business Card

Derek Hollis QWP MWPS(FP) ( regisestered trademark of the p on afp)
Financial Planner

m 0412 564 918
p 1300 426 715
f 02 9638 1407
e derek@tbplanners.com.au
www. tbplanners.com.au

Suite 4 /9 Marlowe Crescent
Kelsey Vale NSW 2615

Suite 1703 Level 17 North Block,
Harbourgate Plaza Centre
214 Ketley Road NSW 2047

Logo Text

Tidewater Bay Planners

Logo styles of interest
Pictorial/Combination Logo
Requirements
Must have
• muST logo can be rejigged but must keep opera house

```html
<!DOCTYPE html>
<html lang="en">
<head>
<meta charset="utf-8">
<title>Tidewater Bay Planners – Business Card Options</title>
<link rel="stylesheet" href="https://fonts.googleapis.com/css2?family=Mulish:wght@700&family=Questrial&display=swap">
<style>
  :root {
    --page: #f1f1f1;
    --sheet: #ffffff;
    --ink: #262626;
    --ink-soft: #3a3a3a;
    --green: #86b385;
    --band-dark: #232323;
    --silver-dark: #c2c2c2;
    --silver-mid: #d9d9d9;
    --silver-light: #f7f7f7;
    --edge: #d6d6d6;
  }
  * { box-sizing: border-box; margin: 0; padding: 0; }
  html, body { width: 1200px; height: 1145px; overflow: hidden; }
  body {
    background: var(--page);
    font-family: "Questrial", "Century Gothic", sans-serif;
    color: var(--ink);
  }
  .sheet {
    position: absolute; left: 2px; top: 2px; width: 1196px; height: 1141px;
    background: var(--sheet);
  }
  .option-number {
    position: absolute; left: 141px;
    font-size: 44px; color: var(--ink);
  }
  .option-number--one { top: 74px; }
  .option-number--two { top: 600px; }

  .card {
    position: absolute; overflow: hidden;
    border: 1px solid var(--edge);
    background: linear-gradient(115deg,
      var(--silver-dark) 0%, var(--silver-light) 32%, var(--silver-mid) 48%,
      var(--silver-light) 66%, #ffffff 74%, var(--silver-dark) 100%);
  }
  .card--one { left: 195px; top: 73px; width: 831px; height: 462px; }
  .card--two { left: 200px; top: 598px; width: 828px; height: 460px; }

  .card > * { position: absolute; }

  .brand { display: flex; align-items: center; gap: 12px; }
  .brand__dot { width: 22px; height: 22px; border-radius: 50%; background: var(--green); }
  .brand__name { font-family: "Mulish", sans-serif; font-weight: 700; font-size: 21px; color: var(--ink); white-space: nowrap; }

  .person__name { font-family: "Mulish", sans-serif; font-weight: 700; font-size: 27px; color: var(--ink); }
  .person__title { font-size: 21px; color: var(--ink-soft); }
  .person__credentials { font-size: 13.5px; line-height: 22px; color: var(--ink-soft); }

  .contacts { list-style: none; }
  .contacts li { display: flex; align-items: center; height: 31.5px; font-size: 23.5px; color: var(--ink-soft); white-space: nowrap; }
  .contacts svg { width: 18px; height: 18px; margin-right: 11px; flex: none; }

  .address { font-size: 19.5px; line-height: 21px; color: var(--ink-soft); white-space: nowrap; }
  .address .gap { margin-top: 12px; }
  .address--compact { font-size: 17.5px; line-height: 19.5px; }
  .address--compact .gap { margin-top: 10px; }

  .bands { left: 0; width: 100%; }
  .website { font-family: "Mulish", sans-serif; font-weight: 700; font-size: 23px; color: var(--ink); white-space: nowrap; }
  .credentials-foot { left: 0; width: 100%; text-align: center; font-size: 14px; color: var(--ink-soft); }
</style>
</head>
<body>
<svg width="0" height="0" style="position:absolute">
  <defs>
    <symbol id="icon-mobile" viewBox="0 0 18 18"><rect x="4" y="1" width="10" height="16" rx="2" fill="none" stroke="currentColor" stroke-width="1.6"/><line x1="7" y1="14" x2="11" y2="14" stroke="currentColor" stroke-width="1.4"/></symbol>
    <symbol id="icon-phone" viewBox="0 0 18 18"><path d="M5 2l3 3-2 2c1 2.5 3 4.5 5 5l2-2 3 3-2 3C8 15.5 2.5 10 2 4z" fill="currentColor"/></symbol>
    <symbol id="icon-fax" viewBox="0 0 18 18"><rect x="4" y="1" width="10" height="5" fill="none" stroke="currentColor" stroke-width="1.4"/><rect x="1" y="6" width="16" height="8" rx="1" fill="currentColor"/><rect x="4" y="12" width="10" height="5" fill="#fff" stroke="currentColor" stroke-width="1.4"/></symbol>
    <symbol id="icon-mail" viewBox="0 0 18 18"><rect x="1" y="4" width="16" height="11" fill="none" stroke="currentColor" stroke-width="1.4"/><path d="M1 4l8 6 8-6" fill="none" stroke="currentColor" stroke-width="1.4"/></symbol>
  </defs>
</svg>

<main class="sheet">
  <div class="option-number option-number--one">1</div>
  <div class="option-number option-number--two">2</div>

  <section class="card card--one" aria-label="Business card option 1">
    <div class="brand" style="left:456px; top:150px;">
      <span class="brand__dot"></span>
      <span class="brand__name">Tidewater Bay Planners</span>
    </div>

    <h1 class="person__name" style="left:82px; top:95px;">Derek Hollis</h1>
    <p class="person__title" style="left:81px; top:136px;">Financial Planner</p>
    <div class="person__credentials" style="left:81px; top:164px;">
      <p>QWP MWPS(FP)</p>
      <p>(registered mark of the p on qwp)</p>
    </div>

    <ul class="contacts" style="left:48px; top:243px;">
      <li><svg><use href="#icon-mobile"/></svg>0412 564 918</li>
      <li><svg><use href="#icon-phone"/></svg>1300 426 715</li>
      <li><svg><use href="#icon-fax"/></svg>02 9638 1407</li>
      <li><svg><use href="#icon-mail"/></svg>derek@tbplanners.com.au</li>
    </ul>

    <div class="address" style="left:392px; top:243px;">
      <p>Suite 4 /9 Marlowe Crescent Kelsey Vale</p>
      <p>NSW 2615</p>
      <p class="gap">Suite 1703 Level 17 North Block,</p>
      <p>Harbourgate Plaza Centre 214 Ketley Road</p>
      <p>NSW 2047</p>
    </div>

    <svg class="bands" style="top:404px; height:58px;" viewBox="0 0 831 58" preserveAspectRatio="none">
      <polygon points="0,0 374,0 425,30 831,30 831,58 0,58" fill="var(--green)"/>
      <polygon points="395,0 831,0 831,22 436,22" fill="var(--band-dark)"/>
    </svg>
    <p class="website" style="left:78px; top:411px;">www.tbplanners.com.au</p>
  </section>

  <section class="card card--two" aria-label="Business card option 2">
    <div class="brand" style="left:51px; top:128px;">
      <span class="brand__dot"></span>
      <span class="brand__name">Tidewater Bay Planners</span>
    </div>

    <div class="address address--compact" style="left:428px; top:49px;">
      <p>Suite 4 /9 Marlowe Crescent Kelsey Vale</p>
      <p>NSW 2615</p>
      <p class="gap">Suite 1703 Level 17 North Block,</p>
      <p>Harbourgate Plaza Centre 214 Ketley Road</p>
      <p>NSW 2047</p>
    </div>

    <h1 class="person__name" style="left:56px; top:209px;">Derek Hollis</h1>
    <p class="person__title" style="left:55px; top:250px;">Financial Planner</p>

    <ul class="contacts" style="left:428px; top:206px;">
      <li><svg><use href="#icon-mobile"/></svg>0412 564 918</li>
      <li><svg><use href="#icon-phone"/></svg>1300 426 715</li>
      <li><svg><use href="#icon-fax"/></svg>02 9638 1407</li>
      <li><svg><use href="#icon-mail"/></svg>derek@tbplanners.com.au</li>
    </ul>

    <svg class="bands" style="top:362px; height:48px;" viewBox="0 0 828 48" preserveAspectRatio="none">
      <polygon points="0,0 403,0 367,19 0,19" fill="var(--band-dark)"/>
      <polygon points="441,0 828,0 828,48 0,48 0,29 392,29" fill="var(--green)"/>
    </svg>
    <p class="website" style="left:457px; top:370px;">www.tbplanners.com.au</p>

    <p class="credentials-foot" style="top:422px;">QWP MWPS(FP) (registered mark of the p on qwp)</p>
  </section>
</main>
</body>
</html>
```